Web Design Project

Hi, we need a new and professional design for our company "partnerlinkhubgroup". The website should communicate business but with a friendly and professional touch.

You can use the following categories for the menu;

Home - customer groups - products - voucher system- contact

Give it your best,

Regards,
Dorian

Industry/Entity Type

Business

```html
<!DOCTYPE html>
<html lang="en">
<head>
<meta charset="utf-8">
<title>partnerlinkhubgroup</title>
<link rel="stylesheet" href="https://fonts.googleapis.com/css2?family=Arimo:wght@400;700&family=Roboto+Condensed:wght@400;700&display=swap">
<style>
:root{
  --page:#e7e4da;
  --panel:#ffffff;
  --ink:#3a3a3a;
  --ink-soft:#555555;
  --muted:#8a8a8a;
  --link:#1d4fa8;
  --date:#2a7ed3;
  --blue-deep:#0a1d8c;
  --blue-mid:#1a49c4;
  --blue-light:#4f8fe8;
  --sand:#cfc8a3;
  --rule:#c9c9c9;
}
*{margin:0;padding:0;box-sizing:border-box}
html,body{width:1200px;height:1128px;overflow:hidden}
body{background:var(--page);font-family:"Arimo",Arial,sans-serif;color:var(--ink-soft);position:relative}
.abs{position:absolute}
.date{left:86px;top:70px;font-size:14px;color:#666}
.date b{color:#555;margin-right:2px}
.date .time{margin-left:24px;font-weight:700;color:#555}
.panel{left:345px;top:34px;width:836px;height:1020px;background:var(--panel);border-radius:8px;box-shadow:0 2px 8px rgba(0,0,0,.15)}
.toolbar svg{position:absolute;top:70px}
.tool-sep{position:absolute;top:66px;width:1px;height:26px;background:#d6d6d6}
.banner{left:19px;top:114px;width:1162px;height:188px;border-radius:6px 0 0 6px;overflow:hidden;
  background:radial-gradient(ellipse at 30% 40%,var(--blue-light) 0%,var(--blue-mid) 40%,var(--blue-deep) 100%)}
.brand-zone{left:0;top:0;width:326px;height:188px;background:linear-gradient(100deg,#e8f1fb 0%,#9cc2ee 55%,rgba(60,120,220,.4) 100%)}
.brand{left:36px;top:72px;font-family:"Roboto Condensed",Arial,sans-serif;font-weight:700;font-size:30px;color:#ffffff;letter-spacing:-.3px}
.brand-dot{left:18px;top:84px;width:12px;height:12px;background:#ffffff;border-radius:50%}
.banner-art{left:380px;top:12px;width:330px;height:176px;border-radius:4px;background:linear-gradient(160deg,#c9d3e6 0%,#7d8ca8 55%,#2b3f8a 100%)}
.cable-art{left:720px;top:0;width:440px;height:70px;background:linear-gradient(90deg,rgba(200,210,230,0) 0%,rgba(200,210,230,.35) 100%)}
.tagline{left:717px;top:-16px;width:445px;height:105px;margin-top:0}
.tag-box{left:717px;top:-16px}
.tagbox{left:736px;top:154px;width:445px;height:104px;border:1px solid rgba(140,180,255,.6);border-right:0;background:linear-gradient(180deg,#102aa6,#0a1d8c)}
.tagbox p{position:absolute;left:26px;color:#fff;font-family:"Roboto Condensed",Arial,sans-serif;letter-spacing:.5px}
.tagbox .t1{top:14px;font-size:40px;font-weight:400}
.tagbox .t2{top:58px;font-size:25px}
.nav{left:34px;top:312px;width:311px}
.nav a{display:block;height:78px;margin-bottom:10px;padding:14px 0 0 32px;text-decoration:none;border-radius:6px 0 0 6px;
  background:linear-gradient(180deg,#fbfaf6 0%,#ecebe4 100%);border:1px solid #d9d7cd;border-right:0;box-shadow:0 1px 2px rgba(0,0,0,.08)}
.nav .label{display:block;font-family:"Roboto Condensed",Arial,sans-serif;font-size:22px;color:#2f2f2f;letter-spacing:-.3px}
.nav .sub{display:block;font-size:16px;color:#8d8d8d;margin-top:-2px}
.contact{left:34px;top:851px;width:311px;height:155px;background:var(--sand);border-radius:8px 0 0 8px;padding:14px 0 0 46px}
.contact h3{font-family:"Roboto Condensed",Arial,sans-serif;font-weight:400;font-size:26px;color:#4a4a3a;margin-bottom:6px}
.contact p{font-size:16px;line-height:21px;color:#555548}
.contact strong{color:#4a4a3a}
h2.head{font-family:"Roboto Condensed",Arial,sans-serif;font-weight:700;font-size:31px;color:#3d3d3d;letter-spacing:-1px;line-height:32px}
.kicker{font-family:"Roboto Condensed",Arial,sans-serif;font-size:19px;color:#8a8a8a;line-height:20px}
.copy{font-size:16.5px;line-height:21px;color:#444}
.more{font-size:16.5px;color:#888}
.more a{color:var(--link);text-decoration:none}
.more .dot{color:#aaa;font-size:11px;margin:0 4px}
.welcome-art{left:376px;top:400px;width:230px;height:184px;border-radius:50%;background:radial-gradient(circle,#e8eef3 0%,#9fb3c4 55%,#5a7389 100%)}
.welcome{left:631px;top:374px;width:500px}
.welcome .copy{margin-top:24px}
.welcome .more{text-align:right;margin-top:8px;padding-right:0}
.priority{left:393px;top:628px;width:335px}
.rule{border-bottom:1px solid var(--rule);padding-bottom:8px}
.priority .copy{margin-top:28px}
.links{list-style:none;margin-top:18px;padding-left:0}
.links li{height:28.5px;border-bottom:1px dotted #bbb;padding:3px 0 0 18px;font-size:16.5px;position:relative}
.links li::before{content:"+";position:absolute;left:2px;top:4px;font-size:11px;color:#999}
.links a{color:var(--link);text-decoration:none}
.vdivider{left:761px;top:616px;width:1px;height:368px;background:#bdbdbd}
.news{left:794px;top:628px;width:337px}
.item{position:absolute;left:0;width:337px}
.item .art{position:absolute;border-radius:50%}
.item .body{position:absolute;left:151px;right:0}
.item .date-n{font-family:"Roboto Condensed",Arial,sans-serif;font-weight:700;font-size:21px;color:var(--date);margin-right:6px}
.item .more{text-align:right;margin-top:8px}
.sep-dots{left:794px;top:865px;width:337px;border-top:1px dotted #bbb}
.footer{left:0;width:1200px;top:1071px;text-align:center;font-size:16.5px;color:#555}
</style>
</head>
<body>
<div class="abs date"><b>FRI</b> 00.00.2013 <span class="time">5:45</span> PM</div>

<div class="abs panel"></div>

<div class="toolbar">
  <svg style="left:397px" width="18" height="16" viewBox="0 0 18 16"><path d="M2 8 L9 2 L16 8 M4 7 V14 H14 V7" fill="none" stroke="#777" stroke-width="1.4"/></svg>
  <span class="tool-sep" style="left:454px"></span>
  <svg style="left:492px" width="14" height="16" viewBox="0 0 14 16"><path d="M2 1 H9 L12 4 V15 H2 Z" fill="none" stroke="#777" stroke-width="1.4"/></svg>
  <span class="tool-sep" style="left:545px"></span>
  <svg style="left:580px" width="18" height="16" viewBox="0 0 18 16"><g fill="none" stroke="#777" stroke-width="1.3"><rect x="6" y="1" width="6" height="4"/><rect x="1" y="11" width="6" height="4"/><rect x="11" y="11" width="6" height="4"/><path d="M9 5 V8 M4 11 V8 H14 V11"/></g></svg>
</div>

<div class="abs banner">
  <div class="abs brand-zone"></div>
  <span class="abs brand-dot"></span>
  <div class="abs brand">partnerlinkhubgroup</div>
  <div class="abs banner-art" role="img" aria-label="Photo of an open laptop showing two user silhouettes with a network cable"></div>
  <div class="abs cable-art" role="img" aria-label="Network cable curving across the banner"></div>
</div>
<div class="abs tagbox">
  <p class="t1">INDIVIDUAL</p>
  <p class="t2">CUSTOMERS APPROACH</p>
</div>

<nav class="abs nav">
  <a href="#"><span class="label">Home</span><span class="sub">lorem empus</span></a>
  <a href="#"><span class="label">Customer Groups</span><span class="sub">lorem epsum</span></a>
  <a href="#"><span class="label">Products</span><span class="sub">lorum epsum</span></a>
  <a href="#"><span class="label">Voucher System</span><span class="sub">lerum epsum</span></a>
  <a href="#"><span class="label">Contact</span><span class="sub">lerum epsum</span></a>
</nav>

<address class="abs contact" style="font-style:normal">
  <h3>Primary Contact</h3>
  <p><strong>Northgate Trading Ltd.</strong><br>4120 - 4124 Elm Street,<br>Leeds, LS12 4AB<br><strong>Phone:</strong> +1 800 412 7730</p>
</address>

<div class="abs welcome-art" role="img" aria-label="Illustration of people icons linked in a network ring"></div>
<section class="abs welcome">
  <h2 class="head">Welcome to our Company Website</h2>
  <p class="kicker">Some words about company</p>
  <p class="copy">Donec et tortor. Praesent iaculis vestibulum neque arcu tortor… fringilla ut, suscipit ac, condimentum sit amet, est. Praesent malesuada purus at dolor. Maecenas porttitor, ante nec pulvinar suscipit, ante nisl lobortis dui, eu malesuada pede tortor mollis wisi. Suspendisse egestas. Quisque enim…</p>
  <p class="more">|<span class="dot">+</span><a href="#">read more about company</a>|</p>
</section>

<section class="abs priority">
  <div class="rule">
    <h2 class="head">Priority line of business</h2>
    <p class="kicker">Professional management and researches</p>
  </div>
  <p class="copy">Praesent malesuada purus at dolor. Suspendisse egestas. Quisque enim. Duis neque pede, ultrices sed, vulputate at, vestibulum id, nunc quisque orci quam, consectetuer quis, rhoncus sed…</p>
  <ul class="links">
    <li><a href="#">Praesent malesuada purus at dolor.</a></li>
    <li><a href="#">Suspendisse egestas quisque enim.</a></li>
    <li><a href="#">Duis neque pede ultrices sed vulput</a></li>
    <li><a href="#">Quisque orci quam, consectetuer quis</a></li>
    <li><a href="#">Rhoncus sed vehicula nec velit.</a></li>
  </ul>
</section>

<div class="abs vdivider"></div>

<section class="abs news">
  <div class="rule">
    <h2 class="head">Latest News</h2>
    <p class="kicker">corporate highlights</p>
  </div>
  <article class="item" style="top:82px">
    <div class="art" style="left:-6px;top:0;width:141px;height:136px;background:radial-gradient(circle,#ffffff 0%,#e6e6e6 60%,#bdbdbd 100%)" role="img" aria-label="Illustration of a white cloud labelled network"></div>
    <div class="body" style="top:20px">
      <p class="copy"><span class="date-n">21.05</span>Praesent iaculis vestibulum neque arcu tortor fringilla ut, suscipit ac, condimentum sit…</p>
      <p class="more">|<span class="dot">+</span><a href="#">read more</a>|</p>
    </div>
  </article>
  <div class="abs sep-dots" style="left:0;top:237px"></div>
  <article class="item" style="top:246px">
    <div class="art" style="left:17px;top:0;width:102px;height:105px;background:radial-gradient(circle at 45% 40%,#c8cde0 0%,#5a6490 55%,#2a2f52 100%)" role="img" aria-label="Illustration of a glossy globe with network lines"></div>
    <div class="body" style="top:14px">
      <p class="copy"><span class="date-n">15.05</span>Praesent male-suada purus at dolor. Maecenas porttitor, ante nec pulvinar suscipit…</p>
      <p class="more">|<span class="dot">+</span><a href="#">read more</a>|</p>
    </div>
  </article>
</section>

<footer class="abs footer">partnerlinkhubgroup.Com © 2013 | Privacy Policy | Terms Of Use</footer>
</body>
</html>
```